BRACKENRIDGE BUILDERS B-Card

I currently have a b-card design but will be removing the image (tree) from the logo and have text only.
I want the card to be classy and strong within the building and construction industry.
I will be using Spot UV on the cards as per the attached examples. I will also send through some sketched ideas that I have in mind.
The color blue is similar to the image (No. 6) attached images

Target Market(s)

middle to maturre aged.
Home Owners / Renovators and Builders

Industry/Entity Type

Construction

Contact Information for Business Card

BRACKENRIDGE BUILDERS
Name: Dermot Quaile
Title: Project Manager
Mobile: 0412 537 804
Office: (08) 9173 5842
Address: 17C Pellworth Avenue, Malaga WA 6090
Email: info@brackenridgebuild.com.au
PO Box: 3817 Malaga WA 6944

Colors
0592cd
33a6d7
85cae6
1b1b1b

Requirements
Must have
• 1. It must have spot UV on the front of card, maybe back of card too
• 2. I really like the blue on image 6. (or at least a really cool electric blue against the charcoal grey background)
• 3. The font must be slimline and modern. Easy to read
• 4. There must be no black used on the card... Only greys and dark charcoal greys
• 5. Use only the text from the logo "Brackenridge Builders" Not the image of the tree. I am wanting the b-cards to be more masculine.
Nice to have
• 1. I like the design concept on image 6. but happy to see what else you can do with the Spot UV
• 2. Unless you have a really cool idea of the image of the tree (from previous logo) Spot UV somewhere in the design concept thats original and different then I am keen to see what you come up with
• 3. Try changing the color of the logo eg. full white or Blue and white
• 4. Another option is to have the Brackenridge Logo on the front of card with the spot UV in the background of text which we specialise in eg, Roofing, Ceiling, Insulation, Gutter Guards, Electrical, Insurance etc and we can add or reduce items as required. Similar to image 12.
Should not have
• Do not include the image of the tree from previous logo. unless you have a really cool idea of Spot UV somewhere in the design concept thats original and different.

```html
<!DOCTYPE html>
<html lang="en">
<head>
<meta charset="utf-8">
<title>Brackenridge Builders – Business Card</title>
<link href="https://fonts.googleapis.com/css2?family=Open+Sans:wght@400;600&display=swap" rel="stylesheet">
<style>
  :root {
    --backdrop: #5b4232;
    --card: #262626;
    --spot-uv: #1f1f1f;
    --blue: #33a6d7;
    --text: #f2f2f2;
  }
  * { box-sizing: border-box; margin: 0; padding: 0; }
  html, body {
    width: 1200px; height: 1000px; overflow: hidden;
    background: var(--backdrop);
    font-family: "Open Sans", Arial, sans-serif;
  }
  .card {
    position: absolute; left: 265px; width: 666px; height: 397px;
    background: var(--card);
    box-shadow: 0 4px 14px rgba(0,0,0,.35);
    color: var(--text);
  }
  .card--front { top: 73px; }
  .card--back { top: 532px; }

  .wordmark {
    position: absolute; right: 33px;
    color: var(--blue); font-weight: 600;
    font-size: 30px; line-height: 34px; letter-spacing: 2px;
    text-align: right;
  }
  .card--front .wordmark { top: 60px; }
  .card--back .wordmark { top: 300px; }

  .contact { position: absolute; left: 33px; top: 174px; }
  .contact__name { color: var(--blue); font-weight: 600; font-size: 19px; line-height: 24px; }
  .contact__title { font-size: 16px; line-height: 22px; }
  .contact__list { list-style: none; margin-top: 17px; }
  .contact__list li {
    display: flex; align-items: center; gap: 7px;
    font-size: 16px; line-height: 23px;
  }
  .contact__list svg { width: 16px; height: 16px; fill: var(--blue); flex: none; }
  .contact__address { margin-top: 6px; font-size: 16px; line-height: 27px; }

  .spot-uv-art {
    position: absolute; left: 20px; top: 4px; width: 385px; height: 385px;
    border-radius: 50%;
    background: radial-gradient(circle at 60% 45%, #181818 0%, var(--spot-uv) 55%, var(--card) 75%);
  }
</style>
</head>
<body>
  <section class="card card--front">
    <div class="wordmark">BRACKENRIDGE<br>BUILDERS</div>
    <div class="contact">
      <p class="contact__name">DERMOT QUAILE</p>
      <p class="contact__title">Project Manager</p>
      <ul class="contact__list">
        <li>
          <svg viewBox="0 0 16 16" aria-hidden="true"><path d="M5 1h6a1 1 0 0 1 1 1v12a1 1 0 0 1-1 1H5a1 1 0 0 1-1-1V2a1 1 0 0 1 1-1zm.5 1.5v10h5v-10zM8 13.2a.6.6 0 1 0 0 1.2.6.6 0 0 0 0-1.2z"/></svg>
          0412 537 804
        </li>
        <li>
          <svg viewBox="0 0 16 16" aria-hidden="true"><path d="M2 6c0-2 3-3.5 6-3.5S14 4 14 6v1h-3V5.5H5V7H2zM4.5 8h7l2 5H2.5zM8 9a1.5 1.5 0 1 0 0 3 1.5 1.5 0 0 0 0-3z"/></svg>
          (08) 9173 5842
        </li>
        <li>
          <svg viewBox="0 0 16 16" aria-hidden="true"><path d="M1 4h14v1l-7 4.5L1 5zm0 2.3 7 4.5 7-4.5V12H1z"/></svg>
          info@brackenridgebuild.com.au
        </li>
      </ul>
      <p class="contact__address">PO Box 3817 Malaga WA 6944<br>17C Pellworth Avenue, Malaga WA 6090</p>
    </div>
  </section>

  <section class="card card--back">
    <div class="spot-uv-art" role="img" aria-label="Large gloss spot UV tree with spreading branches, leaves and roots"></div>
    <div class="wordmark">BRACKENRIDGE<br>BUILDERS</div>
  </section>
</body>
</html>
```